Australian wine project aimed at the Asian market

We are looking for a wine label that is attractive to the Asian market specifically mainland China. There should be space left for varietal and alcohol by % info. The products will be red and sparkling red the label should reflect the country of origin but must be elegant.
Reason: The first brief was a bit vague.
Target Market(s)
Adults based in China with a leaning towards traditional design.
Requirements
Must have
- I would love to see a pen and ink style of design incorporating a traditional Australian homestead. It would be great to see a Kangaroo if possible encroaching on the land.

```html
<!DOCTYPE html>
<html lang="en">
<head>
<meta charset="UTF-8">
<title>Marlow Ridge Sparkling Shiraz Label</title>
<link href="https://fonts.googleapis.com/css2?family=Cinzel:wght@400;500&family=Arimo:wght@400;700&display=swap" rel="stylesheet">
<style>
  :root {
    --page: #ffffff;
    --label-black: #000000;
    --gold: #f2c21b;
    --gold-deep: #e0a800;
    --ring-red: #e8362a;
    --ring-light: #f6d3cc;
    --text-white: #ffffff;
    --scene-light: #f4f4f2;
    --scene-dark: #6a6a66;
  }
  html, body {
    margin: 0;
    padding: 0;
    width: 1200px;
    height: 1000px;
    overflow: hidden;
    background: var(--page);
  }
  .canvas {
    position: relative;
    width: 1200px;
    height: 1000px;
  }
  .label-shape {
    position: absolute;
    left: 0;
    top: 0;
  }
  .brand-name,
  .varietal,
  .vintage {
    position: absolute;
    left: 0;
    width: 1200px;
    margin: 0;
    text-align: center;
    font-family: "Cinzel", serif;
    font-weight: 400;
    color: var(--gold);
    line-height: 1;
  }
  .brand-name {
    top: 168px;
    font-size: 38px;
    letter-spacing: 1px;
  }
  .varietal {
    top: 568px;
    font-size: 46px;
    line-height: 58px;
  }
  .vintage {
    top: 708px;
    font-size: 29px;
  }
  .volume,
  .strength,
  .origin {
    position: absolute;
    margin: 0;
    font-family: "Arimo", Arial, sans-serif;
    color: var(--text-white);
    line-height: 1;
  }
  .volume {
    left: 444px;
    top: 832px;
    font-size: 19px;
    font-weight: 700;
  }
  .strength {
    right: 443px;
    top: 832px;
    font-size: 19px;
    font-weight: 700;
  }
  .origin {
    left: 0;
    width: 1200px;
    top: 867px;
    text-align: center;
    font-size: 16px;
    font-weight: 700;
  }
</style>
</head>
<body>
<main class="canvas">
  <svg class="label-shape" width="1200" height="1000" viewBox="0 0 1200 1000">
    <defs>
      <radialGradient id="homestead-tone" cx="50%" cy="55%" r="60%">
        <stop offset="0%" stop-color="var(--scene-dark)"/>
        <stop offset="55%" stop-color="#b9b9b4"/>
        <stop offset="100%" stop-color="var(--scene-light)"/>
      </radialGradient>
    </defs>
    <path class="label-body"
      d="M400,112 H455 Q470,112 476,96 Q512,52 600,52 Q688,52 724,96 Q730,112 745,112 H800 V903 H745 Q730,903 724,919 Q688,948 600,948 Q512,948 476,919 Q470,903 455,903 H400 Z"
      fill="var(--label-black)" stroke="var(--gold)" stroke-width="5"/>
    <g class="medallion">
      <ellipse cx="600" cy="392" rx="170" ry="138" fill="var(--gold)"/>
      <ellipse cx="600" cy="392" rx="164" ry="132" fill="var(--ring-red)"/>
      <ellipse cx="600" cy="392" rx="157" ry="125" fill="none" stroke="var(--ring-light)" stroke-width="7"/>
      <ellipse cx="600" cy="392" rx="150" ry="118" fill="var(--gold-deep)"/>
      <ellipse cx="600" cy="392" rx="146" ry="114" fill="url(#homestead-tone)"
        role="img" aria-label="Pen and ink illustration of a traditional Australian homestead with verandah and garden"/>
    </g>
  </svg>

  <h1 class="brand-name">Marlow Ridge</h1>
  <h2 class="varietal">Sparkling<br>Shiraz</h2>
  <p class="vintage">2016</p>

  <p class="volume">750ml</p>
  <p class="strength">12% Vol</p>
  <p class="origin">Product of Australia</p>
</main>
</body>
</html>
```